Geschäftsbrief und Rechnungsvorlage
Zielgruppe
Kalvoria steht für die psychologische Weiterbildung, Unterstützung und Prävention der psychischen Gesundheit.
Für unsere Unterlagen benötigen wir eine Geschäftsbriefvorlage und Rechnungsvorlage.
Aufgabenstellung
Wenn möglich ein modernes und schlichtes Design.
Als Inhalt können Sie gerne Dummy-Texte verwenden.

```html
<!DOCTYPE html>
<html lang="de">
<head>
<meta charset="utf-8">
<title>Kalvoria – Geschäftsbrief</title>
<link rel="stylesheet" href="https://fonts.googleapis.com/css2?family=Open+Sans:wght@400;600;700&family=Arimo:wght@400&display=swap">
<style>
  :root {
    --backdrop: #5b5c60;
    --paper: #ffffff;
    --accent: #ee7a22;
    --brand-dark: #0f4257;
    --ink: #1d1d1d;
    --muted: #3a3a3a;
    --watermark: #f1f1f1;
    --ink-blue: #1c2a8c;
  }
  * { box-sizing: border-box; margin: 0; padding: 0; }
  html, body { width: 1200px; height: 945px; overflow: hidden; background: var(--backdrop); }
  .letter {
    position: absolute; left: 280px; top: 20px;
    width: 640px; height: 905px;
    background: var(--paper);
    overflow: hidden;
    font-family: "Open Sans", sans-serif;
    color: var(--ink);
  }
  .letter__top-band { position: absolute; left: 0; top: 0; width: 100%; height: 6px; background: var(--accent); }
  .fold-mark { position: absolute; left: 0; width: 14px; height: 1px; background: #bdbdbd; }
  .fold-mark--upper { top: 320px; }
  .fold-mark--middle { top: 452px; }
  .fold-mark--lower { top: 640px; }

  .brand {
    position: absolute; right: 52px; top: 92px;
    display: flex; align-items: center; gap: 8px;
  }
  .brand__square { width: 16px; height: 16px; background: var(--accent); }
  .brand__name { font-weight: 700; font-size: 38px; color: var(--brand-dark); letter-spacing: -0.5px; }

  .sender-line {
    position: absolute; left: 72px; top: 134px;
    font-size: 7px; color: var(--muted);
    border-bottom: 0.6px solid var(--muted); padding-bottom: 1px;
  }
  .sender-line .sep { color: var(--accent); padding: 0 2px; }

  .recipient { position: absolute; left: 72px; top: 160px; font-size: 10.5px; line-height: 1.35; }
  .recipient__city { margin-top: 12px; }

  .contact {
    position: absolute; left: 468px; top: 230px;
    border-left: 1px solid #555; padding-left: 12px;
    font-size: 9px; line-height: 1.4; color: var(--muted);
  }
  .contact__row { display: flex; align-items: center; gap: 5px; }
  .contact__row svg { width: 9px; height: 9px; flex: none; }

  .letter__body {
    position: absolute; left: 72px; top: 298px; width: 500px;
    font-family: "Arimo", sans-serif; font-size: 12px; line-height: 1.33;
  }
  .subject { margin-bottom: 14px; }
  .salutation { margin-bottom: 14px; }
  .paragraph { text-align: justify; margin-bottom: 14px; }
  .closing { margin-top: 4px; }
  .signature { display: block; width: 150px; height: 42px; margin: 12px 0 6px; background: linear-gradient(90deg, rgba(28,42,140,0.18), rgba(28,42,140,0.08)); border-radius: 3px; }

  .watermark {
    position: absolute; left: 40px; top: 640px;
    font-weight: 700; font-size: 120px; color: var(--watermark);
    letter-spacing: -2px; user-select: none;
  }

  .footer { position: absolute; left: 0; bottom: 0; width: 100%; }
  .footer__columns {
    display: flex; padding: 0 40px 14px 40px;
    font-size: 8.5px; line-height: 1.4; color: var(--muted);
  }
  .footer__col { flex: 1; }
  .footer__col + .footer__col { border-left: 1px solid #555; padding-left: 18px; }
  .footer__band {
    height: 24px; background: var(--brand-dark);
    display: flex; align-items: center; padding-left: 200px;
    font-size: 10px; color: #fff; letter-spacing: 0.3px;
  }
</style>
</head>
<body>
<main class="letter">
  <div class="letter__top-band"></div>
  <span class="fold-mark fold-mark--upper"></span>
  <span class="fold-mark fold-mark--middle"></span>
  <span class="fold-mark fold-mark--lower"></span>

  <div class="brand">
    <span class="brand__square"></span>
    <span class="brand__name">Kalvoria</span>
  </div>

  <p class="sender-line">Kalvoria GmbH<span class="sep">|</span>Muster Weg 32<span class="sep">|</span>10400 Muster Stadt</p>

  <address class="recipient" style="font-style:normal">
    Musterfirma<br>
    z. Hd. Herrn Mustermann<br>
    Musterweg 13
    <div class="recipient__city">24102 Musterstadt</div>
  </address>

  <div class="contact">
    <div>Kalvoria GmbH</div>
    <div>Muster Weg 32</div>
    <div>10400 Muster Stadt</div>
    <div class="contact__row">
      <svg viewBox="0 0 10 10"><path d="M2 1l2 0 1 2-1.2 1a5 5 0 0 0 2.2 2.2L7 5l2 1v2c-4 0.5-8-3.5-7-7z" fill="var(--accent)"/></svg>
      +49 (0) 123 000 456 00
    </div>
    <div class="contact__row">
      <svg viewBox="0 0 10 10"><rect x="2" y="1" width="6" height="3" fill="var(--accent)"/><rect x="1" y="4" width="8" height="4" rx="1" fill="var(--accent)"/></svg>
      +49 (0) 123 000 456 99
    </div>
    <div class="contact__row">
      <svg viewBox="0 0 10 10"><rect x="0.5" y="2" width="9" height="6" fill="var(--accent)"/><path d="M0.5 2l4.5 3.5 4.5-3.5" stroke="#fff" stroke-width="0.8" fill="none"/></svg>
      info@kalvoria.de
    </div>
  </div>

  <div class="watermark" aria-hidden="true">Kalvoria</div>

  <section class="letter__body">
    <p class="subject">Betreffzeile</p>
    <p class="salutation">Sehr geehrte Damen und Herren,</p>
    <p class="paragraph">In sollicitudin, metus et posuere blandit, erat dui bibendum eros, id vestibulum sem justo vel mauris. Ut tempor dolor ut justo vulputate, eu blandit libero faucibus. In laoreet, massa non ultricies tempor, est enim auctor mi, sit amet venenatis massa augue in justo. Praesent eu tincidunt diam. Maecenas id mi efficitur tellus interdum consectetur vel sed ante. Sed suscipit quis eros a fermentum. Curabitur ornare sit amet leo eu semper. Vestibulum pretium mi eu nisi. gadde.</p>
    <p class="paragraph">Sed nunc est, iaculis vel enim ut, fringilla commodo lorem. Pellentesque facilisis tempus lorem eget porttitor. Morbi accumsan, nulla accumsan mollis maximus, lectus diam venenatis odio, quis bibendum elit ex a arcu. Fusce turpis erat, euismod sit amet dolor eu, hendrerit rhoncus libero. Phasellus convallis, mi vel pharetra sollicitudin, nisi purus maximus est, nec lobortis dolor enim et augue. Vestibulum auctor mi sit amet leo auctor egestas. Pellentesque eget endrerit rhoncus dan.</p>
    <p class="closing">Mit freundlichen Grüßen</p>
    <span class="signature" role="img" aria-label="Handschriftliche Unterschrift in blauer Tinte"></span>
    <p class="signer">Jonas Berkel, LL.M.</p>
  </section>

  <footer class="footer">
    <div class="footer__columns">
      <div class="footer__col">Bankverbindung:<br>Sparkasse Nordtal-Heide</div>
      <div class="footer__col">BIC: KLVODE21XXX<br>IBAN: DE12 3456 0078 0901 00000 00</div>
      <div class="footer__col">Steuernummer: 204/318/00000<br>Umsatzsteuer-ID-Nr.: DE 412790000</div>
    </div>
    <div class="footer__band">www.kalvoria.de</div>
  </footer>
</main>
</body>
</html>
```